Business Card and Letterhead Design for Public Accounting Firm

Business card and letterhead design for a CPA Firm located in Orange County, CA. We're looking for a modern and professional design utilizing our existing logo. We'd like a clean "less is more" look, but also something that catches the eye. We provide a high level of service to our clients. Open to single or double sided business cards.

Additional info: color numbers on logo
Blue :
R 0
G 83
B 125

#00537D

Silver :

R 154
G 154
B 154

#9A9A9A

Target Market(s)

Businesses and individuals

Industry/Entity Type

Accounting

Contact Information for Business Card

Moss Whitfield & Danby LLP - 4827 Larkspur Vale Road, Irvine, CA 92614 - (949)731-2864 - mwdaccts.example

Font styles to use
Serif
Sans Serif
Other font styles liked:
• See font file uploaded

Colors
0054AA
0677BA
7BADD7
CADEEF
E8F1F8

Requirements
Nice to have
• Possibly use the font file provided which matches our logo, but adjust to be not in all caps

```html
<!DOCTYPE html>
<html lang="en">
<head>
<meta charset="utf-8">
<title>Moss Whitfield &amp; Danby LLP – Business Card</title>
<link rel="stylesheet" href="https://fonts.googleapis.com/css2?family=Cinzel:wght@400;600&display=swap">
<style>
  :root {
    --page-bg: #ededed;
    --brand-blue: #00567f;
    --silver-light: #cbcbcb;
    --silver-mid: #9a9a9a;
    --silver-dark: #6e6e6e;
    --white: #ffffff;
  }
  * { margin: 0; padding: 0; box-sizing: border-box; }
  html, body {
    width: 1200px; height: 918px; overflow: hidden;
    background: var(--page-bg);
    font-family: "Cinzel", "Times New Roman", serif;
    color: var(--white);
  }
  .canvas { position: relative; width: 1200px; height: 918px; }

  .card {
    position: absolute;
    width: 529px; height: 317px;
    overflow: hidden;
  }
  .card--front {
    left: 60px; top: 300px;
    background: linear-gradient(150deg, var(--silver-light) 0%, var(--silver-mid) 55%, var(--silver-dark) 100%);
  }
  .card--back {
    left: 611px; top: 301px;
    background: var(--brand-blue);
  }

  .firm-name {
    position: absolute;
    font-weight: 400;
    text-transform: uppercase;
    color: var(--white);
    line-height: 1.15;
    white-space: nowrap;
  }
  .card--front .firm-name {
    left: 0; right: 0; top: 128px;
    text-align: center;
    font-size: 25px;
    letter-spacing: 4px;
  }
  .card--back .firm-name {
    left: 32px; top: 140px;
    font-size: 13.5px;
    letter-spacing: 2px;
  }

  .person { position: absolute; left: 273px; top: 66px; }
  .person__name {
    font-size: 17px; font-weight: 600;
    letter-spacing: 3.5px; text-transform: uppercase;
    line-height: 1;
    white-space: nowrap;
  }
  .person__rule {
    width: 110px; height: 1px; background: var(--white);
    margin-top: 7px;
  }
  .person__role {
    margin-top: 6px;
    font-size: 11px; letter-spacing: 0.5px;
    text-transform: uppercase;
  }

  .contacts { position: absolute; left: 272px; top: 170px; list-style: none; }
  .contacts__item {
    display: flex; align-items: center;
    height: 17px; margin-bottom: 12px;
    font-size: 13.5px; letter-spacing: 0.2px;
    line-height: 17px;
    text-transform: uppercase;
    white-space: nowrap;
  }
  .contacts__icon { width: 17px; height: 17px; margin-right: 13px; flex: none; }
</style>
</head>
<body>
<main class="canvas">

  <section class="card card--front" aria-label="Business card front">
    <p class="firm-name">Moss Whitfield<br>&amp; Danby LLP</p>
  </section>

  <section class="card card--back" aria-label="Business card back">
    <p class="firm-name">Moss Whitfield<br>&amp; Danby LLP</p>

    <div class="person">
      <p class="person__name">Jonathan R</p>
      <div class="person__rule"></div>
      <p class="person__role">Accountant</p>
    </div>

    <ul class="contacts">
      <li class="contacts__item">
        <svg class="contacts__icon" viewBox="0 0 20 20" aria-hidden="true">
          <circle cx="10" cy="10" r="10" fill="#fff"/>
          <path d="M6.5 5.5l2 0 1 2.6-1.3 1a6 6 0 0 0 2.7 2.7l1-1.3 2.6 1v2c0 .6-.4 1-1 1A9 9 0 0 1 5.5 6.5c0-.6.4-1 1-1z" fill="var(--brand-blue)"/>
        </svg>
        (949)731-2864
      </li>
      <li class="contacts__item">
        <svg class="contacts__icon" viewBox="0 0 20 20" aria-hidden="true">
          <circle cx="10" cy="10" r="10" fill="#fff"/>
          <rect x="5.5" y="6.8" width="9" height="6.4" fill="var(--brand-blue)"/>
          <path d="M5.5 6.8l4.5 3.6 4.5-3.6" fill="none" stroke="#fff" stroke-width="0.9"/>
        </svg>
        mwd@mail-co.example
      </li>
      <li class="contacts__item">
        <svg class="contacts__icon" viewBox="0 0 20 20" aria-hidden="true">
          <circle cx="10" cy="10" r="10" fill="#fff"/>
          <g fill="none" stroke="var(--brand-blue)" stroke-width="0.9">
            <circle cx="10" cy="10" r="4.6"/>
            <ellipse cx="10" cy="10" rx="2" ry="4.6"/>
            <path d="M5.4 10h9.2M6 7.7h8M6 12.3h8"/>
          </g>
        </svg>
        mwdaccts.example
      </li>
    </ul>
  </section>

</main>
</body>
</html>
```